Ophthalmologist Needs Celebrity Endorsed LASIK Poster Advertisement

Dr. Gerald P. Wexley, MD is an eye physician and surgeon in Kauai, Hawaii. He is the premier ophthalmologist on Kauai and is the only LASIK surgeon. LASIK is a vision correction surgery to help patients reduce or eliminate their dependence on glasses and contact lenses. He has performed hundreds of LASIK procedures and recently did the procedure on one of the actresses from the hit movie "Tide Dancer". She has provided us with content and the rights to produce advertisements using her celebrity endorsement of Dr. Wexley and the LASIK procedure. We need a poster advertisement that will be placed in the lobby of our office building (which receives a lot of foot traffic to other offices). This poster should be eye-catching to passerby, but also convey the LASIK message. Our intent is to generate interest in the procedure (people who wear glasses and contact lenses). The final design should communicate the premier image of our ophthalmology practice and generate interest in LASIK. More information on our practice and LASIK can be found at: www.wexleyeyecare-demo.com.
Updates

Reason: I am still getting back to a few designers on their designs and would like to see the changes before I make a final decision. Thanks for your patience!

Target Market(s)

Men and women ages 25-45 who wear glasses or contact lenses

Industry/Entity Type

Building

Requirements
Must have
• The poster should have our company name (Wexley Eye Care) and logo (attached). It should also use at least one of the attached photos of the celebrity. It should also have the following endorsement verbatum:
"Mahalo Dr. Wexley and staff. I will never take my new eyesight for granted. I love it! Thanks for your care and love." Aloha and God Bless, Marta Ibsen, "Nohea" Da Bad Girl

```html
<!DOCTYPE html>
<html lang="en">
<head>
<meta charset="utf-8">
<title>Wexley Eye Care – LASIK Poster</title>
<link rel="stylesheet" href="https://fonts.googleapis.com/css2?family=Fira+Sans+Condensed:ital,wght@1,300&family=Poppins:wght@400;700&display=swap">
<style>
  :root {
    --brand-yellow: #f5d320;
    --ink: #231d0c;
    --white: #ffffff;
    --photo-dark: #2b1d16;
    --photo-skin: #b88466;
    --photo-warm: #c9a88a;
    --photo-cool: #c5d2dc;
  }
  html, body {
    margin: 0;
    padding: 0;
    overflow: hidden;
    background: #ffffff;
  }
  .poster {
    position: relative;
    width: 800px;
    height: 1200px;
    overflow: hidden;
    background: var(--brand-yellow);
  }
  .hero-photo {
    position: absolute;
    left: 0;
    top: 0;
    width: 800px;
    height: 900px;
    background:
      radial-gradient(ellipse 260px 360px at 380px 300px, var(--photo-skin) 0%, rgba(184,132,102,0) 75%),
      radial-gradient(ellipse 300px 500px at 680px 250px, var(--photo-cool) 0%, rgba(197,210,220,0) 80%),
      linear-gradient(90deg, var(--photo-dark) 0%, #4a3226 30%, var(--photo-warm) 70%, #a98f78 100%);
  }
  .testimonial {
    position: absolute;
    left: 13px;
    top: 404px;
    width: 470px;
    margin: 0;
  }
  .testimonial-quote {
    margin: 0;
    font-family: "Fira Sans Condensed", sans-serif;
    font-style: italic;
    font-weight: 300;
    font-size: 40px;
    line-height: 48.7px;
    letter-spacing: -0.5px;
    color: var(--white);
  }
  .testimonial-name {
    margin: 6px 0 0;
    font-family: "Poppins", sans-serif;
    font-weight: 700;
    font-size: 29px;
    line-height: 44px;
    letter-spacing: -0.5px;
    color: var(--brand-yellow);
  }
  .testimonial-role {
    margin: 0;
    font-family: "Fira Sans Condensed", sans-serif;
    font-style: italic;
    font-weight: 300;
    font-size: 33px;
    line-height: 46px;
    color: var(--white);
  }
  .tagline {
    position: absolute;
    left: 40px;
    top: 960px;
    margin: 0;
    font-family: "Poppins", sans-serif;
    font-weight: 400;
    font-size: 31px;
    line-height: 48px;
    letter-spacing: -0.5px;
    color: var(--ink);
  }
  .brand {
    position: absolute;
    left: 510px;
    top: 872px;
    width: 280px;
    text-align: center;
  }
  .brand-mark {
    display: block;
    margin: 0 auto;
  }
  .brand-name {
    margin: 4px 0 0;
    font-family: "Poppins", sans-serif;
    font-weight: 400;
    font-size: 27px;
    letter-spacing: -0.5px;
    color: var(--ink);
  }
</style>
</head>
<body>
  <main class="poster">
    <div class="hero-photo" role="img" aria-label="Portrait of the actress Marta Ibsen with long dark hair, smiling over her shoulder against a softly blurred background"></div>

    <blockquote class="testimonial">
      <p class="testimonial-quote">"Mahalo Dr. Wexley and staff. I will never take my new eyesight for granted. I love it! Thanks for your care and love."</p>
      <p class="testimonial-name">Marta Ibsen,</p>
      <p class="testimonial-role">"Nohea" Da Bad Girl</p>
    </blockquote>

    <p class="tagline">We don’t have to tell you<br>about our LASIK surgery.<br>You’ll see for your self</p>

    <div class="brand">
      <svg class="brand-mark" width="200" height="200" viewBox="0 0 200 200" aria-hidden="true">
        <circle cx="100" cy="100" r="94" fill="none" stroke="var(--ink)" stroke-width="7"/>
      </svg>
      <p class="brand-name">Wexley Eye Care</p>
    </div>
  </main>
</body>
</html>
```